Redesign Category Images For VelvetNook.ie Online Sex Shop Ireland

Description

We are an Online Adult Sex Shop Based in Ireland our business is focused on adult sex toys for men and women.

We are looking for a talented graphic designer to redesign our category and banner images for our home page refresh. If you win the contest we will hire you on a contract going forward.

Bright colours and images are essential we are open to creativity!

Please ensure image sizes are the same as the attached images. Please create graphics for the list below.

Best Price Guarantee
Black Friday
Valentines Day
New Products
Vibrators
Sex Toys For Men
Free Gift
Free Discreet Shipping
Guaranteed Christmas Delivery

Buy Gift Cards
Dildos
Best Anal Sex Toys
Couples Sex Toys
Best of Bondage Sexy Gifts
Sex Toys For Her
Sexy Gifts
Vibrators
Lubes & Lotions - For Slipy Slide Fun - Shop Now
Lingerie - Undress To Impress - Shop Now
Camming Sex Toys For Her - Enhance Your Shows - Shop Now
Camming Sex Toys For Him - Enhance Your Shows - Shop Now

Please make sure that the design is CREATIVE and please DO NOT COPY FROM OTHER COMPANIES, we need ensure all images are unique and and it will fail if you do so, thanks so much for your effort! Feel free to use any product images you wish for each category.

Good luck and have fun with this :)

```html
<!DOCTYPE html>
<html lang="en">
<head>
<meta charset="utf-8">
<title>VelvetNook.ie – Category Banners</title>
<link href="https://fonts.googleapis.com/css2?family=Open+Sans:ital,wght@0,400;0,600;0,700;1,400;1,700&display=swap" rel="stylesheet">
<style>
  :root {
    --paper: #ffffff;
    --edge: #bdbdbd;
    --violet-deep: #3f2585;
    --violet: #6a3fa6;
    --magenta: #e8197d;
    --pink: #ea4f9f;
    --sky: #3ab4e6;
    --blue-ink: #34379a;
    --ribbon: #29a3df;
    --white: #ffffff;
  }
  * { box-sizing: border-box; margin: 0; padding: 0; }
  html, body { width: 988px; height: 1200px; overflow: hidden; background: var(--paper); }
  body { font-family: "Open Sans", Arial, sans-serif; }

  .canvas {
    position: relative; width: 988px; height: 1200px;
    border: 1px solid var(--edge); background: var(--paper);
  }
  .banner { position: absolute; overflow: hidden; }

  /* Best price guarantee */
  .banner--price {
    left: 11px; top: 16px; width: 961px; height: 286px;
    background:
      radial-gradient(ellipse 420px 200px at 640px 300px, rgba(234,79,159,.75), transparent 70%),
      radial-gradient(ellipse 300px 180px at 920px 40px, rgba(58,180,230,.45), transparent 70%),
      radial-gradient(ellipse 260px 160px at 100px 40px, rgba(234,79,159,.45), transparent 70%),
      linear-gradient(120deg, var(--violet-deep), var(--violet) 55%, #4a2c93);
  }
  .brand-name {
    position: absolute; color: var(--magenta);
    font-weight: 700; letter-spacing: .5px; white-space: nowrap;
  }
  .banner--price .brand-name { left: 36px; top: 134px; font-size: 32px; }
  .price-blob { position: absolute; left: 351px; top: 33px; width: 196px; height: 162px; }
  .price-best, .price-price {
    position: absolute; color: var(--white); font-style: italic; line-height: 1;
  }
  .price-best { left: 418px; top: 106px; font-size: 42px; font-weight: 400; }
  .price-price { left: 418px; top: 148px; font-size: 52px; font-weight: 700; }
  .price-guarantee {
    position: absolute; left: 524px; top: 198px; color: var(--white);
    font-size: 42px; line-height: 1; transform: scaleX(.88); transform-origin: left;
  }

  /* Vibrators */
  .banner--vibrators {
    left: 11px; top: 371px; width: 585px; height: 235px;
    background:
      radial-gradient(ellipse 260px 140px at 380px 230px, rgba(234,79,159,.8), transparent 70%),
      radial-gradient(ellipse 240px 140px at 60px 220px, rgba(58,180,230,.8), transparent 70%),
      linear-gradient(135deg, #8c73c9, #b37ac0 50%, #7aa9dd);
  }
  .vib-title, .vib-cta { position: absolute; left: 44px; color: var(--white); font-size: 39px; line-height: 1; }
  .vib-title { top: 44px; }
  .vib-tag { position: absolute; left: 46px; top: 101px; color: var(--blue-ink); font-size: 22px; }
  .vib-cta { top: 138px; font-size: 37px; }
  .vib-products {
    position: absolute; left: 302px; top: 30px; width: 176px; height: 165px; border-radius: 14px;
    background: linear-gradient(90deg, rgba(40,30,40,.55), rgba(130,70,170,.6) 50%, rgba(40,190,190,.6));
  }

  /* Sex toys for her */
  .banner--her {
    left: 620px; top: 315px; width: 352px; height: 349px;
    background:
      radial-gradient(ellipse 200px 160px at 300px 260px, rgba(234,79,159,.85), transparent 70%),
      radial-gradient(ellipse 180px 140px at 40px 80px, rgba(58,180,230,.7), transparent 70%),
      linear-gradient(150deg, #8d77cf, #c07cc2 55%, #6aa8e0);
  }
  .frame { position: absolute; border: 1.5px solid rgba(255,255,255,.9); }
  .banner--her .frame { inset: 10px; }
  .her-title, .her-sub { position: absolute; right: 30px; font-size: 40px; line-height: 1; }
  .her-title { top: 42px; color: var(--white); }
  .her-sub { top: 100px; color: var(--blue-ink); }
  .her-products {
    position: absolute; left: 27px; top: 140px; width: 264px; height: 186px; border-radius: 14px;
    background: linear-gradient(90deg, rgba(25,25,30,.7), rgba(45,45,55,.7) 55%, rgba(60,130,220,.7));
  }

  /* Black Friday */
  .banner--friday {
    left: 11px; top: 681px; width: 961px; height: 505px;
    background:
      radial-gradient(ellipse 360px 220px at 120px 80px, rgba(58,180,230,.75), transparent 70%),
      radial-gradient(ellipse 380px 260px at 880px 160px, rgba(234,79,159,.8), transparent 70%),
      radial-gradient(ellipse 420px 200px at 520px 470px, rgba(58,180,230,.8), transparent 70%),
      linear-gradient(135deg, #8a6fcf, #a86fc5 45%, #d660a8);
  }
  .banner--friday .frame { left: 55px; top: 44px; width: 851px; height: 428px; }
  .sale-word { position: absolute; left: 112px; font-size: 92px; line-height: 1; color: var(--white); }
  .sale-word--black { top: 74px; }
  .sale-word--friday { top: 175px; color: var(--blue-ink); }
  .sale-word--sale { top: 277px; }
  .sale-dots { position: absolute; left: 158px; top: 352px; display: flex; gap: 17px; }
  .sale-dots span { width: 14px; height: 14px; border-radius: 50%; background: rgba(255,255,255,.75); }
  .sale-dots { top: 412px; }
  .ribbon { position: absolute; left: 560px; top: 0; width: 188px; height: 210px; }
  .ribbon-label {
    position: absolute; left: 560px; top: 72px; width: 188px; text-align: center;
    color: var(--white); font-size: 46px; line-height: 1;
  }
  .special-offers { position: absolute; left: 472px; top: 228px; color: var(--white); font-size: 36px; line-height: 1; }
  .brand-glow {
    position: absolute; left: 444px; top: 291px; width: 434px; height: 110px;
    background: radial-gradient(ellipse at center, rgba(255,255,255,1) 45%, rgba(255,255,255,0) 75%);
  }
  .banner--friday .brand-name { left: 482px; top: 318px; font-size: 46px; }
</style>
</head>
<body>
<main class="canvas">

  <section class="banner banner--price" aria-label="Best price guarantee">
    <span class="brand-name">VelvetNook.ie</span>
    <svg class="price-blob" viewBox="0 0 196 162" aria-hidden="true">
      <path d="M30 30 C70 -5 160 0 186 40 C205 75 180 140 120 155 C60 170 5 140 3 95 C1 65 10 45 30 30 Z" fill="#e8197d"/>
    </svg>
    <span class="price-best">BEST</span>
    <span class="price-price">PRICE</span>
    <span class="price-guarantee">GUARANTEE</span>
  </section>

  <section class="banner banner--vibrators" aria-label="Vibrators">
    <h2 class="vib-title" style="font-weight:400">VIBRATORS</h2>
    <p class="vib-tag">YOUR INSTANT LOVE</p>
    <p class="vib-cta">SHOP NOW</p>
    <div class="vib-products" role="img" aria-label="Product shots of three vibrators in black, purple and teal"></div>
  </section>

  <section class="banner banner--her" aria-label="Sex toys for her">
    <div class="frame"></div>
    <h2 class="her-title" style="font-weight:400">SEX TOYS</h2>
    <p class="her-sub">FOR HER</p>
    <div class="her-products" role="img" aria-label="Product shots of a wand massager, a phone app and a blue egg toy"></div>
  </section>

  <section class="banner banner--friday" aria-label="Black Friday sale">
    <div class="frame"></div>
    <span class="sale-word sale-word--black">BLACK</span>
    <span class="sale-word sale-word--friday">FRIDAY</span>
    <span class="sale-word sale-word--sale">SALE</span>
    <div class="sale-dots"><span></span><span></span><span></span><span></span><span></span><span></span></div>
    <svg class="ribbon" viewBox="0 0 188 210" aria-hidden="true">
      <path d="M0 0 H188 V180 L94 210 L0 180 Z" fill="#29a3df"/>
    </svg>
    <span class="ribbon-label">50%</span>
    <p class="special-offers">SPECIAL OFFERS</p>
    <div class="brand-glow"></div>
    <span class="brand-name">VelvetNook.ie</span>
  </section>

</main>
</body>
</html>
```